New Record Label needs a Web design

We are Moss Lantern: a London based, new & independent music production company aimed at the 25-40 age group. The musical style is Soul/Classic Motown.
We have at the moment just one signed artist, but will expand in the future.
We dont' have any webpage yet and are looking for an innovative web design for our webpage www.moss-lantern.com
I have uploaded our company logo.

Initially the whole website will only have 3 tabs: Home page/Artists/Contact

The design should be classic and high-end, but can be a bit crazy too.

```html
<!DOCTYPE html>
<html lang="en">
<head>
<meta charset="utf-8">
<title>Moss Lantern — Home</title>
<link rel="stylesheet" href="https://fonts.googleapis.com/css2?family=Bebas+Neue&family=Montserrat:wght@600;700&family=Arimo:wght@400;700&display=swap">
<style>
:root{
  --black:#000;
  --orange:#f26b35;
  --nav-orange:#f39a4c;
  --red:#e8323a;
  --white:#fff;
  --body-grey:#c9c9c9;
  --dark-text:#1a0d06;
}
*{margin:0;padding:0;box-sizing:border-box}
html,body{width:712px;height:1200px;overflow:hidden;background:var(--black)}
.page{position:relative;width:712px;height:1200px;background:var(--black);font-family:"Arimo",Arial,sans-serif}
.abs{position:absolute}
.display{font-family:"Bebas Neue",Impact,sans-serif;font-weight:400;line-height:1}
.name{font-family:"Montserrat",Arial,sans-serif;font-weight:700;line-height:1.1;text-transform:uppercase}
.blurb{font-size:6.6px;line-height:1.3;color:var(--body-grey)}

/* header */
.main-nav,.brand,.social{z-index:3}
.main-nav{left:86px;top:6px;display:flex;gap:28px}
.main-nav a{font-family:"Bebas Neue",Impact,sans-serif;font-size:19px;line-height:1.1;color:var(--nav-orange);text-decoration:none;letter-spacing:.5px}
.brand{left:296px;top:5px;width:120px;text-align:center;font-family:"Bebas Neue",Impact,sans-serif;font-size:13px;line-height:1;color:var(--red);letter-spacing:1px;white-space:nowrap}
.brand .dot{display:block;width:16px;height:16px;border-radius:50%;background:var(--red);margin:0 auto 3px}
.social{right:82px;top:6px;display:flex;gap:5px}
.social span{width:14px;height:14px;border-radius:50%;background:var(--red)}

/* banner */
.stage{left:0;top:28px;width:712px;height:237px;background:linear-gradient(90deg,#3d8fd6 0%,#1b2f6b 18%,#6a2a8c 35%,#c02d6a 55%,#e2532a 75%,#f07a1e 100%)}
.hero{left:86px;top:68px;width:542px;height:216px;border:2px solid #12121e;background:radial-gradient(ellipse at 55% 40%,#e7b79a 0%,#c98e6a 25%,#d8cdb8 55%,#bdb6a4 100%)}

/* sections */
.section-title{font-size:38px}
.artists-title{left:83px;top:309px;color:var(--orange)}
.feature-img{left:82px;top:353px;width:215px;height:156px;border:1px solid #3a2a20}
.feature-name{font-size:13.5px;white-space:nowrap}
.item{left:325px;width:300px;height:54px}
.thumb{position:absolute;left:0;top:0;width:74px;height:54px;border:1px solid #3a3a3a}
.item .name{position:absolute;left:82px;top:3px;font-size:10px;white-space:nowrap}
.item .blurb{position:absolute;left:82px;top:15px;width:218px}
.more{left:325px;font-size:19px}

.dots-top{left:0;top:636px;width:712px;height:50px;background:linear-gradient(180deg,var(--black) 0%,#7a3418 45%,var(--orange) 100%)}
.songs-band{left:0;top:684px;width:712px;height:338px;background:var(--orange)}
.dots-bottom{left:0;top:1020px;width:712px;height:58px;background:linear-gradient(180deg,var(--orange) 0%,#7a3418 55%,var(--black) 100%)}
.songs .blurb{color:var(--dark-text)}
.songs .name{color:var(--dark-text)}
.play{position:absolute;left:50%;top:50%;transform:translate(-50%,-50%)}

/* footer */
.foot-brand{left:69px;top:1104px;width:110px;text-align:center;white-space:nowrap}
.foot-brand .mark{display:block;font-family:"Bebas Neue",Impact,sans-serif;font-size:14px;line-height:1;color:var(--red);letter-spacing:1px}
.foot-brand .dot{display:block;width:18px;height:18px;border-radius:50%;background:var(--red);margin:0 auto 4px}
.foot-brand small{display:block;font-size:6.5px;color:var(--orange);margin-top:5px}
.foot-nav-title{left:220px;top:1102px;font-size:31px;color:var(--orange)}
.foot-links{left:221px;top:1134px;display:grid;grid-template-columns:49px 40px;row-gap:1px}
.foot-links a{font-size:8px;color:var(--orange);text-decoration:none}
.connect-title{left:381px;top:1102px;font-size:30px;color:var(--red);white-space:nowrap}
.subscribe-note{left:383px;top:1134px;font-size:9px;color:var(--red)}
.subscribe-note b{font-weight:700}
.email{left:382px;top:1151px;width:187px;height:19px;background:var(--orange);border:none}
.subscribe-btn{left:573px;top:1151px;width:59px;height:19px;background:var(--white);border:none;font-family:"Arimo",Arial,sans-serif;font-size:8px;color:#000}
</style>
</head>
<body>
<div class="page">

  <header>
    <nav class="abs main-nav"><a href="#">Home</a><a href="#">Artists</a><a href="#">Contact</a></nav>
    <div class="abs brand"><span class="dot"></span>Moss Lantern</div>
    <div class="abs social" aria-label="Social links"><span></span><span></span><span></span><span></span><span></span></div>
  </header>

  <div class="abs stage" role="img" aria-label="Stage light rays with dancing performer silhouettes"></div>
  <div class="abs hero" role="img" aria-label="Smiling woman wearing headphones against soft bokeh lights"></div>

  <section class="artists">
    <h2 class="abs display section-title artists-title">Artists</h2>
    <div class="abs feature-img" role="img" aria-label="Guitarist performing outdoors with arm raised" style="background:linear-gradient(160deg,#6b5a48 0%,#a7866a 45%,#4e3424 100%)"></div>
    <h3 class="abs name feature-name" style="left:82px;top:520px;color:var(--orange)">Jonah Hale Kessler</h3>
    <p class="abs blurb" style="left:82px;top:539px;width:210px">Hit the floor and enjoy hiphop DJ Pocho's spin sessions. With millions of light combinations on the dance floor, DJ Pocho will entertain with freestyle sessions.</p>

    <div class="abs item" style="top:353px">
      <div class="thumb" role="img" aria-label="Singer wearing red headphones" style="background:linear-gradient(135deg,#2b4f7a,#c8b3a6)"></div>
      <h4 class="name" style="color:var(--orange)">Yara Costell</h4>
      <p class="blurb">Over 3 hours of cruising through the NYC harbor. Enjoy the open-air deck and admire magnificent views of Manhattan's stunning skyline at sunset with your sweetheart.</p>
    </div>
    <div class="abs item" style="top:424px">
      <div class="thumb" role="img" aria-label="Band posing outdoors under a blue sky" style="background:linear-gradient(160deg,#2f6fc0,#8fa35a 60%,#4a5a2a)"></div>
      <h4 class="name" style="color:var(--orange)">Red Timberline</h4>
      <p class="blurb">Arrive on the pier and walk down the red carpet with your group. A team of professional photographers will capture your red carpet grand entrance.</p>
    </div>
    <div class="abs item" style="top:496px">
      <div class="thumb" role="img" aria-label="Five band members standing in a row" style="background:linear-gradient(180deg,#5a5a5a,#1e1e1e)"></div>
      <h4 class="name" style="color:var(--orange)">Merry Yes Band</h4>
      <p class="blurb">Hit the floor and enjoy hiphop DJ Pocho's spin sessions. With millions of light combinations on the dance floor, DJ Pocho will entertain with freestyle sessions.</p>
    </div>
    <a class="abs display more" style="top:581px;color:var(--orange);text-decoration:none" href="#">Click here for more gallery</a>
  </section>

  <div class="abs dots-top" role="img" aria-label="Halftone dot border fading into orange"></div>
  <div class="abs songs-band"></div>
  <div class="abs dots-bottom" role="img" aria-label="Halftone dot border fading into black"></div>

  <section class="songs">
    <h2 class="abs display section-title" style="left:83px;top:702px;color:#000">Songs</h2>
    <div class="abs feature-img" role="img" aria-label="Music video still of a singer among warm bokeh lights" style="top:746px;background:linear-gradient(135deg,#3a200e 0%,#b07040 45%,#e6b98a 70%,#5a3218 100%)">
      <svg class="play" width="42" height="42" viewBox="0 0 42 42" aria-hidden="true"><circle cx="21" cy="21" r="19" fill="none" stroke="#fff" stroke-width="3" opacity=".85"/><path d="M16 12 L31 21 L16 30Z" fill="#fff" opacity=".85"/></svg>
    </div>
    <h3 class="abs name feature-name" style="left:82px;top:913px">Elsie Garland - Your Song</h3>
    <p class="abs blurb" style="left:82px;top:932px;width:220px">As you disembark you will receive your custom gift bag to take home with you which will include souvenirs.</p>

    <div class="abs item" style="top:746px">
      <div class="thumb" role="img" aria-label="Music video still in warm orange tones" style="background:linear-gradient(135deg,#f0a050,#c0401a);border-color:#7a3418">
        <svg class="play" width="30" height="30" viewBox="0 0 30 30" aria-hidden="true"><circle cx="15" cy="15" r="13" fill="none" stroke="#fff" stroke-width="2.5"/><path d="M12 9 L22 15 L12 21Z" fill="#fff"/></svg>
      </div>
      <h4 class="name">Tessa Vale - Our Song</h4>
      <p class="blurb">Over 3 hours of cruising through the NYC harbor. Enjoy the open-air deck and admire magnificent views of Manhattan's stunning skyline at sunset with your sweetheart.</p>
    </div>
    <div class="abs item" style="top:816px">
      <div class="thumb" role="img" aria-label="Music video still of a boy band" style="background:linear-gradient(135deg,#3a5a9a,#c0b0a0 50%,#2a3a6a);border-color:#7a3418">
        <svg class="play" width="30" height="30" viewBox="0 0 30 30" aria-hidden="true"><circle cx="15" cy="15" r="13" fill="none" stroke="#fff" stroke-width="2.5" opacity=".8"/><path d="M12 9 L22 15 L12 21Z" fill="#fff" opacity=".8"/></svg>
      </div>
      <h4 class="name">Boy Band Next Wall</h4>
      <p class="blurb">Savor the taste of an exquisite delicacies created by our executive chef exclusively for this event.</p>
    </div>
    <div class="abs item" style="top:888px">
      <div class="thumb" role="img" aria-label="Music video still of a singer in green light" style="background:linear-gradient(135deg,#1f4a26,#9aa080 50%,#183a1c);border-color:#7a3418">
        <svg class="play" width="30" height="30" viewBox="0 0 30 30" aria-hidden="true"><circle cx="15" cy="15" r="13" fill="none" stroke="#fff" stroke-width="2.5" opacity=".8"/><path d="M12 9 L22 15 L12 21Z" fill="#fff" opacity=".8"/></svg>
      </div>
      <h4 class="name">Personalized Gift Bag</h4>
      <p class="blurb">As you disembark you will receive your custom gift bag to take home with you which will include souvenirs.</p>
    </div>
    <a class="abs display more" style="top:967px;color:#000;text-decoration:none" href="#">Click here for more songs</a>
  </section>

  <footer>
    <div class="abs foot-brand"><span class="dot"></span><span class="mark">Moss Lantern</span><small>Copyright © 2014</small></div>
    <h2 class="abs display foot-nav-title">Navigation</h2>
    <nav class="abs foot-links"><a href="#">Home</a><a href="#">Songs</a><a href="#">Artists</a><a href="#">Contact</a></nav>
    <h2 class="abs display connect-title">Connect with Moss Lantern</h2>
    <p class="abs subscribe-note"><b>subscribe</b> to our newsletter</p>
    <input class="abs email" type="email" aria-label="Email address">
    <button class="abs subscribe-btn" type="button">Subscribe</button>
  </footer>

</div>
</body>
</html>
```